Boutique Real Estate Brokerage looking for business card, letterhead and envelope design

We are looking for a cohesive design for our business cards, letterhead and envelopes and that mirrors our high-end homes and clientele. Fern & Gable is being launched and designed for the marketplace of tomorrow. We grew from the #1 team in our community into a full-service firm that is going to revolutionize the traditional real estate model.

We understand that it’s more important than ever to help our clients and partners adapt to behavioral and market changes being driven by generational shifts and technological advances in society, and by combining traditional brokerage services with innovative production and marketing capabilities, we know how to do that better than anyone else.

Requirements
Must have
• business card, letterhead and envelope design - attached logo.

```html
<!DOCTYPE html>
<html lang="en">
<head>
<meta charset="utf-8">
<title>Fern &amp; Gable Realty — Stationery</title>
<link rel="stylesheet" href="https://fonts.googleapis.com/css2?family=Open+Sans:wght@400;600;700&display=swap">
<style>
  :root {
    --navy: #170b55;
    --gold: #c08447;
    --gold-dark: #7a4f25;
    --paper: #ffffff;
    --stage: #000000;
    --shadow: rgba(120,120,120,0.55);
    --rule: #2a2270;
  }
  * { box-sizing: border-box; margin: 0; padding: 0; }
  html, body { width: 1200px; height: 1168px; overflow: hidden; background: var(--stage); }
  body { position: relative; font-family: "Open Sans", Arial, sans-serif; color: var(--navy); }

  .brand { position: absolute; display: flex; align-items: center; gap: 8px; white-space: nowrap; }
  .brand__square { width: 24px; height: 24px; background: var(--gold); flex: none; }
  .brand__name { font-family: "Open Sans", Arial, sans-serif; font-weight: 700; color: var(--navy); font-size: 17px; letter-spacing: 0.2px; }

  .letterhead { position: absolute; left: 151px; top: 80px; width: 756px; height: 979px; background: var(--paper); }
  .letterhead .brand { left: 31px; top: 45px; }
  .letterhead__address { position: absolute; left: 586px; top: 40px; display: flex; gap: 7px; font-size: 12px; line-height: 13px; color: var(--navy); }
  .letterhead__rule { position: absolute; left: 272px; right: 1px; top: 80px; height: 1.5px; background: var(--rule); }
  .letterhead__bands { position: absolute; left: 0; bottom: 0; width: 756px; height: 63px; }

  .envelope { position: absolute; left: 220px; top: 538px; width: 902px; height: 397px; background: var(--paper); box-shadow: 8px 8px 10px var(--shadow); }
  .envelope .brand { left: 46px; top: 285px; gap: 6px; }
  .envelope .brand__square { width: 20px; height: 20px; }
  .envelope .brand__name { font-size: 13px; }
  .envelope__contacts { position: absolute; left: 256px; top: 270px; list-style: none; font-size: 10.5px; }
  .envelope__contacts li { display: flex; align-items: center; gap: 6px; height: 20px; }
  .envelope__bands { position: absolute; left: 386px; top: 280px; width: 516px; height: 43px; }

  .card-stack { position: absolute; left: 351px; top: 251px; width: 288px; height: 482px; }
  .card-stack__layer { position: absolute; width: 288px; height: 482px; background: #e8e8e8; overflow: hidden; box-shadow: 3px 3px 4px var(--shadow); }
  .card-stack__layer--back2 { left: 12px; top: 12px; background: #8a8a8a; }
  .card-stack__layer--back1 { left: 6px; top: 6px; background: #b9b9b9; }
  .card-stack__layer svg { position: absolute; left: 0; bottom: 0; }

  .card-front { position: absolute; left: 0; top: 0; width: 288px; height: 482px; background: var(--paper); border: 1px solid #cfcfcf; overflow: hidden; }
  .card-front .brand { left: 40px; top: 69px; }
  .card-front .brand__name { font-size: 15.5px; }
  .card-front .brand__square { width: 21px; height: 21px; }
  .card-front__name { position: absolute; left: 48px; top: 227px; font-size: 24px; font-weight: 700; color: var(--gold); letter-spacing: 0.3px; }
  .card-front__role { position: absolute; left: 48px; top: 256px; font-size: 16px; color: var(--navy); }
  .card-front__contacts { position: absolute; left: 45px; top: 296px; list-style: none; font-size: 12.5px; letter-spacing: 0.3px; }
  .card-front__contacts li { display: flex; align-items: flex-start; gap: 8px; margin-bottom: 6px; line-height: 15px; }
  .card-front__contacts li.addr { margin-top: 3px; line-height: 13px; }
  .card-front__bands { position: absolute; left: 0; bottom: 0; width: 288px; height: 32px; }

  .card-back { position: absolute; left: 671px; top: 255px; width: 289px; height: 482px; background: var(--navy); box-shadow: 8px 8px 10px var(--shadow); display: flex; align-items: center; justify-content: center; }
  .card-back__name { color: var(--paper); font-weight: 700; font-size: 22px; letter-spacing: 0.5px; }

  .icon { flex: none; display: block; }
</style>
</head>
<body>

<section class="letterhead" aria-label="Letterhead">
  <div class="brand"><span class="brand__square"></span><span class="brand__name">FERN &amp; GABLE REALTY</span></div>
  <div class="letterhead__address">
    <svg class="icon" width="14" height="18" viewBox="0 0 14 18"><path d="M7 0C3.1 0 0 3.1 0 7c0 5 7 11 7 11s7-6 7-11c0-3.9-3.1-7-7-7z" fill="#170b55"/><circle cx="7" cy="7" r="2.6" fill="#fff"/></svg>
    <span>P O Box 00 .adress<br>and00demoadress</span>
  </div>
  <div class="letterhead__rule"></div>
  <svg class="letterhead__bands" viewBox="0 0 756 63" preserveAspectRatio="none">
    <polygon points="0,0 526,0 560,63 0,63" fill="#c08447"/>
    <polygon points="554,0 756,0 756,63 587,63" fill="#170b55"/>
  </svg>
</section>

<section class="envelope" aria-label="Envelope">
  <div class="brand"><span class="brand__square"></span><span class="brand__name">FERN &amp; GABLE REALTY</span></div>
  <ul class="envelope__contacts">
    <li><svg class="icon" width="13" height="13" viewBox="0 0 14 14"><circle cx="7" cy="7" r="7" fill="#170b55"/><path d="M4.5 3.5l1.5 0 .6 1.8-.9.7c.4.9 1.1 1.6 2 2l.7-.9 1.8.6v1.5c-3.3.3-6-2.4-5.7-5.7z" fill="#fff"/></svg>+00(0) 123 456 789</li>
    <li><svg class="icon" width="13" height="13" viewBox="0 0 14 14"><circle cx="7" cy="7" r="7" fill="#170b55"/><rect x="3.5" y="4.5" width="7" height="5" fill="#fff"/><path d="M3.5 4.5L7 7.5 10.5 4.5" stroke="#170b55" stroke-width=".8" fill="none"/></svg>ABC@ABCDE.COM</li>
    <li><svg class="icon" width="13" height="13" viewBox="0 0 14 14"><circle cx="7" cy="7" r="7" fill="#170b55"/><circle cx="7" cy="7" r="3.6" fill="none" stroke="#fff" stroke-width=".8"/><ellipse cx="7" cy="7" rx="1.5" ry="3.6" fill="none" stroke="#fff" stroke-width=".8"/><line x1="3.4" y1="7" x2="10.6" y2="7" stroke="#fff" stroke-width=".8"/></svg>WWW.BCDE.COM</li>
  </ul>
  <svg class="envelope__bands" viewBox="0 0 516 43" preserveAspectRatio="none">
    <polygon points="0,0 321,0 331,43 0,43" fill="#170b55"/>
    <polygon points="358,0 516,0 516,43 367,43" fill="#c08447"/>
  </svg>
</section>

<section class="card-stack" aria-label="Business card, front">
  <div class="card-stack__layer card-stack__layer--back2">
    <svg width="288" height="32" viewBox="0 0 288 32"><polygon points="0,0 201,0 224,32 0,32" fill="#7a4f25"/><polygon points="211,0 288,0 288,32 230,32" fill="#170b55"/></svg>
  </div>
  <div class="card-stack__layer card-stack__layer--back1">
    <svg width="288" height="32" viewBox="0 0 288 32"><polygon points="0,0 201,0 224,32 0,32" fill="#9a6533"/><polygon points="211,0 288,0 288,32 230,32" fill="#170b55"/></svg>
  </div>
  <div class="card-front">
    <div class="brand"><span class="brand__square"></span><span class="brand__name">FERN &amp; GABLE REALTY</span></div>
    <p class="card-front__name">NAME</p>
    <p class="card-front__role">Director</p>
    <ul class="card-front__contacts">
      <li><svg class="icon" width="17" height="17" viewBox="0 0 14 14"><circle cx="7" cy="7" r="7" fill="#c08447"/><path d="M4.5 3.5l1.5 0 .6 1.8-.9.7c.4.9 1.1 1.6 2 2l.7-.9 1.8.6v1.5c-3.3.3-6-2.4-5.7-5.7z" fill="#fff"/></svg>+00(0) 123 456 789</li>
      <li><svg class="icon" width="17" height="17" viewBox="0 0 14 14"><circle cx="7" cy="7" r="7" fill="#c08447"/><rect x="3.5" y="4.5" width="7" height="5" fill="#fff"/><path d="M3.5 4.5L7 7.5 10.5 4.5" stroke="#c08447" stroke-width=".8" fill="none"/></svg>ABC@ABCDE.COM</li>
      <li><svg class="icon" width="17" height="17" viewBox="0 0 14 14"><circle cx="7" cy="7" r="7" fill="#c08447"/><circle cx="7" cy="7" r="3.6" fill="none" stroke="#fff" stroke-width=".8"/><ellipse cx="7" cy="7" rx="1.5" ry="3.6" fill="none" stroke="#fff" stroke-width=".8"/><line x1="3.4" y1="7" x2="10.6" y2="7" stroke="#fff" stroke-width=".8"/></svg>WWW.BCDE.COM</li>
      <li class="addr"><svg class="icon" width="17" height="20" viewBox="0 0 14 18"><path d="M7 0C3.1 0 0 3.1 0 7c0 5 7 11 7 11s7-6 7-11c0-3.9-3.1-7-7-7z" fill="#c08447"/><circle cx="7" cy="7" r="2.6" fill="#fff"/></svg><span>P O Box 00 .adress<br>and00demoadress</span></li>
    </ul>
    <svg class="card-front__bands" viewBox="0 0 288 32" preserveAspectRatio="none">
      <polygon points="0,0 201,0 224,32 0,32" fill="#c08447"/>
      <polygon points="211,0 288,0 288,32 230,32" fill="#170b55"/>
    </svg>
  </div>
</section>

<section class="card-back" aria-label="Business card, back">
  <span class="card-back__name">FERN &amp; GABLE</span>
</section>

</body>
</html>
```